Varlen Group Business Card design with current logo

hello all , we have abranded logo which i will attach but we need a card double sided designed . one side is easy as its the logo but the other side we want clean and modern. The info needed will be the same text as the card sample attached. no pictures of us though just clean and professinal pls. Logo can be incorporated on the text side to for recognition. Colors are Black , white , red and grey... ideal card would be matt finish high end stock. or a black card so white text ... Sorry i have uploaded al the files i got when I had the logo designed on here.. Oh forgot want to say pls add in the card details EST 1981 and over 40yrs combined experiance
Updates

Hello everyone , I'm really sorry we haven't been able to make a final decision.. There is at least 3 cards that all have there positives over the other two... We will decide by tonight.

Target Market(s)

20-70 wide range but people with money and a education.

Industry/Entity Type

Real Estate Agent

Contact Information for Business Card

One side the Logo choose from the different color logos, black being the one we like most, other side is the details. Clean professional looking fonts. EST 1981 , over 40yrs experiance. Website email and both names and PH# as per the sample card attached

Font styles to use
Other font styles liked:
• Fonts:Code Bold,Code Light, Lucida Fax.

Colors
1b1b1b
757575
c9c9c9
e8e8e8
ffffff
e9e9e9

Requirements
Must have
• Logo and contact info

```html
<!DOCTYPE html>
<html lang="en">
<head>
<meta charset="utf-8">
<title>Varlen Group – Business Card</title>
<link rel="stylesheet" href="https://fonts.googleapis.com/css2?family=Lato:wght@400;700&family=Questrial&display=swap">
<style>
  :root {
    --backdrop-light: #e8e8e8;
    --backdrop-dark: #c9c9c9;
    --card-red: #7b1416;
    --card-black: #0d0d0d;
    --ink-white: #ffffff;
    --ink-soft: #e9e9e9;
    --ink-black: #111111;
    --divider-dark: #4a0a0b;
  }
  * { box-sizing: border-box; margin: 0; padding: 0; }
  html, body { width: 1200px; height: 900px; overflow: hidden; }
  body {
    position: relative;
    background: radial-gradient(ellipse at 50% 40%, var(--backdrop-light) 0%, var(--backdrop-dark) 100%);
    font-family: "Lato", sans-serif;
  }

  .card {
    position: absolute;
    width: 700px;
    height: 400px;
    overflow: hidden;
    box-shadow: 0 6px 18px rgba(0,0,0,0.28);
  }

  .brand {
    position: absolute;
    display: flex; align-items: center; gap: 10px;
    font-family: "Lato", sans-serif; font-weight: 700;
    font-size: 22px; letter-spacing: 1px; line-height: 1;
    white-space: nowrap;
  }
  .brand__square { width: 32px; height: 32px; flex: none; }

  /* Front side */
  .card--front { left: 130px; top: 50px; background: var(--card-red); }
  .front__rule {
    position: absolute; left: 0; top: 268px;
    width: 420px; height: 1px; background: var(--ink-black);
  }
  .card--front .brand { right: 50px; top: 252px; color: var(--ink-black); }
  .card--front .brand__square { background: var(--ink-black); }

  /* Back side */
  .card--back { left: 370px; top: 470px; background: var(--card-red); }
  .back__band {
    position: absolute; left: 0; top: 0;
    width: 100%; height: 175px; background: var(--card-black);
  }
  .card--back .brand {
    left: 50%; top: 72px; transform: translateX(-50%);
    color: var(--card-red);
  }
  .card--back .brand__square { background: var(--card-red); }
  .back__divider {
    position: absolute; left: 362px; top: 175px;
    width: 1px; height: 225px; background: var(--divider-dark);
  }

  .agents {
    position: absolute; left: 150px; top: 250px;
    font-family: "Questrial", sans-serif; font-size: 20px;
    line-height: 26px; color: var(--ink-white);
  }
  .agents li { list-style: none; }
  .agents li + li { padding-left: 10px; }
  .heritage {
    position: absolute; left: 150px; top: 316px; width: 200px;
    font-family: "Questrial", sans-serif; font-size: 12px;
    line-height: 17px; letter-spacing: 0.5px; color: var(--ink-soft);
  }

  .contact {
    position: absolute; left: 382px; top: 188px;
    color: var(--ink-white); font-size: 15px;
  }
  .contact__list li {
    list-style: none; display: flex; align-items: center; gap: 10px;
    height: 25px;
  }
  .contact__icon { width: 16px; height: 16px; fill: var(--ink-white); flex: none; }
  .contact__address {
    margin-top: 12px; font-style: normal; line-height: 20px; font-size: 15px;
  }
</style>
</head>
<body>

<section class="card card--front" aria-label="Card front">
  <div class="front__rule"></div>
  <div class="brand"><span class="brand__square"></span>VARLEN GROUP</div>
</section>

<section class="card card--back" aria-label="Card back">
  <div class="back__band"></div>
  <div class="brand"><span class="brand__square"></span>VARLEN GROUP</div>
  <div class="back__divider"></div>

  <ul class="agents">
    <li>Dale Varlen</li>
    <li>Morgan Varlen</li>
  </ul>
  <p class="heritage">EST 1981<br>Over 40 yrs combined experience</p>

  <div class="contact">
    <ul class="contact__list">
      <li>
        <svg class="contact__icon" viewBox="0 0 16 16" aria-hidden="true"><path d="M3 2h3l1 3-2 1.5a8 8 0 0 0 4.5 4.5L11 9l3 1v3a1 1 0 0 1-1 1A11 11 0 0 1 2 3a1 1 0 0 1 1-1z"/></svg>
        <span>555-014-2368</span>
      </li>
      <li>
        <svg class="contact__icon" viewBox="0 0 16 16" aria-hidden="true"><path d="M4 1h6l2 2v3H4z M2 7h12v6h-2v-2H4v2H2z M5 12h6v3H5z"/></svg>
        <span>555-014-7791</span>
      </li>
      <li>
        <svg class="contact__icon" viewBox="0 0 16 16" aria-hidden="true"><path d="M1 3h14v10H1z M1.5 3.5 8 9l6.5-5.5" stroke="#7b1416" stroke-width="1.2"/></svg>
        <span>info@varlenrealestate.com</span>
      </li>
      <li>
        <svg class="contact__icon" viewBox="0 0 16 16" aria-hidden="true"><circle cx="8" cy="8" r="7"/><path d="M1 8h14M8 1c-3 3-3 11 0 14M8 1c3 3 3 11 0 14" stroke="#7b1416" stroke-width="1" fill="none"/></svg>
        <span>www.varlenrealestate.com</span>
      </li>
    </ul>
    <address class="contact__address">
      Harbourline Realty Partners<br>
      210-1820 Alder Crest Way<br>
      Westmoor VC&nbsp; K2L 7P4
    </address>
  </div>
</section>

</body>
</html>
```